Book Cover Design: Backgammon - Ultra Brainy Brainy Test

Book cover design for a self-published book to be sold on Brindlo as a paperback as well as ebook.
The reader takes a quiz of 100 backgammon positions and then see how they fared versus 12 of the best players in the world. The pros then give explanations as to why they made their plays.

Th designs I had are a bit flat so far.

The special thing about this book is 12 of best in world taking the quiz before the reader. That is the attraction…

So how about design where photos of all 12 of them are showing within a backgammon board. You can leave the space for their pics and I insert later or you do once won contract.

But focus on the geniuses would be great, thank you!

Target Market(s)

Backgammon game enthusiasts

Requirements
Must have
• Picture of a backgammon board and idea quiz and top players in the world involved. Author’s name Oren Paskett
Nice to have
• Idea that 12 world class expert backgammon players all contributed to the book

```html
<!DOCTYPE html>
<html lang="en">
<head>
<meta charset="utf-8">
<title>Backgammon – Ultra Brainy Brainy Test</title>
<link href="https://fonts.googleapis.com/css2?family=Bebas+Neue&family=Kurale&family=Oswald:wght@600&display=swap" rel="stylesheet">
<style>
  :root {
    --navy-deep: #19212a;
    --navy-mid: #2e3a4f;
    --navy-glow: #56617f;
    --lamp-gold: #d9a92a;
    --accent-gold: #b8a35c;
    --board-wood: #2b0d0c;
    --board-felt: #3c4660;
    --point-dark: #1f2633;
    --point-light: #a48e4f;
    --slot-fill: #222b3a;
    --ink-white: #ffffff;
    --die-face: #cdc6a8;
    --die-pip: #1a1e24;
  }
  html, body {
    margin: 0;
    padding: 0;
    overflow: hidden;
    background: var(--navy-deep);
  }
  .cover {
    position: relative;
    width: 801px;
    height: 1200px;
    overflow: hidden;
    background:
      radial-gradient(ellipse 380px 430px at 400px 580px, var(--navy-glow) 0%, var(--navy-mid) 45%, var(--navy-deep) 100%);
  }
  .title {
    position: absolute;
    top: 84px;
    left: 0;
    width: 801px;
    margin: 0;
    text-align: center;
    font-family: "Bebas Neue", "Oswald", sans-serif;
    font-weight: 400;
    font-size: 113px;
    line-height: 1;
    letter-spacing: 6px;
    color: var(--ink-white);
  }
  .title-rule {
    position: absolute;
    top: 124px;
  }
  .title-rule--left { left: 44px; }
  .title-rule--right { left: 676px; }
  .subtitle {
    position: absolute;
    top: 192px;
    left: 0;
    width: 801px;
    margin: 0;
    text-align: center;
    font-family: "Kurale", serif;
    font-weight: 400;
    font-size: 47px;
    line-height: 1.1;
    color: var(--ink-white);
  }
  .scene {
    position: absolute;
    top: 255px;
    left: 30px;
    width: 745px;
    height: 625px;
    background:
      radial-gradient(ellipse 110px 170px at 372px 200px, rgba(217,169,42,0.7) 0%, rgba(217,169,42,0.12) 60%, rgba(217,169,42,0) 100%);
  }
  .board {
    position: absolute;
    top: 470px;
    left: 160px;
  }
  .dice-row {
    position: absolute;
    top: 896px;
    left: 172px;
  }
  .tagline {
    position: absolute;
    top: 962px;
    left: 0;
    width: 801px;
    margin: 0;
    text-align: center;
    font-family: "Kurale", serif;
    font-size: 30px;
    line-height: 38px;
    color: var(--ink-white);
  }
  .author {
    position: absolute;
    top: 1084px;
    left: 0;
    width: 801px;
    margin: 0;
    text-align: center;
    font-family: "Oswald", sans-serif;
    font-weight: 600;
    font-size: 64px;
    line-height: 1;
    letter-spacing: 1px;
    color: var(--ink-white);
  }
</style>
</head>
<body>
<main class="cover">
  <svg class="title-rule title-rule--left" width="82" height="36" viewBox="0 0 82 36" aria-hidden="true">
    <g stroke="var(--accent-gold)" stroke-width="3">
      <line x1="2" y1="2" x2="80" y2="2"/>
      <line x1="24" y1="18" x2="80" y2="18"/>
      <line x1="46" y1="34" x2="80" y2="34"/>
    </g>
  </svg>
  <h1 class="title">Backgammon</h1>
  <svg class="title-rule title-rule--right" width="82" height="36" viewBox="0 0 82 36" aria-hidden="true">
    <g stroke="var(--accent-gold)" stroke-width="3">
      <line x1="2" y1="2" x2="80" y2="2"/>
      <line x1="2" y1="18" x2="58" y2="18"/>
      <line x1="2" y1="34" x2="36" y2="34"/>
    </g>
  </svg>
  <p class="subtitle">Ultra Brainy Brainy Test</p>

  <div class="scene" role="img" aria-label="Lamp light falling on a backgammon table, with hands throwing dice above and gold crown chips at the sides"></div>

  <svg class="board" width="480" height="380" viewBox="0 0 480 380" role="img" aria-label="Backgammon board holding twelve portrait spaces for the world-class experts">
    <rect x="0" y="0" width="480" height="380" rx="10" fill="var(--board-wood)"/>
    <rect x="14" y="14" width="218" height="352" fill="var(--board-felt)"/>
    <rect x="248" y="14" width="218" height="352" fill="var(--board-felt)"/>
    <g class="points-top">
      <polygon points="14,14 50,14 32,160" fill="var(--point-light)"/>
      <polygon points="50,14 87,14 68,160" fill="var(--point-dark)"/>
      <polygon points="87,14 123,14 105,160" fill="var(--point-light)"/>
      <polygon points="123,14 159,14 141,160" fill="var(--point-dark)"/>
      <polygon points="159,14 196,14 177,160" fill="var(--point-light)"/>
      <polygon points="196,14 232,14 214,160" fill="var(--point-dark)"/>
      <polygon points="248,14 284,14 266,160" fill="var(--point-light)"/>
      <polygon points="284,14 321,14 302,160" fill="var(--point-dark)"/>
      <polygon points="321,14 357,14 339,160" fill="var(--point-light)"/>
      <polygon points="357,14 393,14 375,160" fill="var(--point-dark)"/>
      <polygon points="393,14 430,14 411,160" fill="var(--point-light)"/>
      <polygon points="430,14 466,14 448,160" fill="var(--point-dark)"/>
    </g>
    <g class="points-bottom">
      <polygon points="14,366 50,366 32,220" fill="var(--point-dark)"/>
      <polygon points="50,366 87,366 68,220" fill="var(--point-light)"/>
      <polygon points="87,366 123,366 105,220" fill="var(--point-dark)"/>
      <polygon points="123,366 159,366 141,220" fill="var(--point-light)"/>
      <polygon points="159,366 196,366 177,220" fill="var(--point-dark)"/>
      <polygon points="196,366 232,366 214,220" fill="var(--point-light)"/>
      <polygon points="248,366 284,366 266,220" fill="var(--point-dark)"/>
      <polygon points="284,366 321,366 302,220" fill="var(--point-light)"/>
      <polygon points="321,366 357,366 339,220" fill="var(--point-dark)"/>
      <polygon points="357,366 393,366 375,220" fill="var(--point-light)"/>
      <polygon points="393,366 430,366 411,220" fill="var(--point-dark)"/>
      <polygon points="430,366 466,366 448,220" fill="var(--point-light)"/>
    </g>
    <g class="expert-slots" fill="var(--slot-fill)" stroke="var(--accent-gold)" stroke-width="4">
      <circle cx="50" cy="115" r="31"/>
      <circle cx="123" cy="115" r="31"/>
      <circle cx="196" cy="115" r="31"/>
      <circle cx="284" cy="115" r="31"/>
      <circle cx="357" cy="115" r="31"/>
      <circle cx="430" cy="115" r="31"/>
      <circle cx="50" cy="265" r="31"/>
      <circle cx="123" cy="265" r="31"/>
      <circle cx="196" cy="265" r="31"/>
      <circle cx="284" cy="265" r="31"/>
      <circle cx="357" cy="265" r="31"/>
      <circle cx="430" cy="265" r="31"/>
    </g>
  </svg>

  <svg class="dice-row" width="460" height="50" viewBox="0 0 460 50" aria-hidden="true">
    <g fill="var(--die-face)" stroke="var(--die-pip)" stroke-width="1.5">
      <rect x="1" y="1" width="46" height="46" rx="9"/>
      <rect x="81" y="1" width="46" height="46" rx="9"/>
      <rect x="161" y="1" width="46" height="46" rx="9"/>
      <rect x="241" y="1" width="46" height="46" rx="9"/>
      <rect x="321" y="1" width="46" height="46" rx="9"/>
      <rect x="401" y="1" width="46" height="46" rx="9"/>
    </g>
    <g fill="var(--die-pip)">
      <circle cx="24" cy="24" r="5"/>
      <circle cx="94" cy="14" r="5"/><circle cx="114" cy="34" r="5"/>
      <circle cx="174" cy="14" r="5"/><circle cx="184" cy="24" r="5"/><circle cx="194" cy="34" r="5"/>
      <circle cx="254" cy="14" r="5"/><circle cx="274" cy="14" r="5"/><circle cx="254" cy="34" r="5"/><circle cx="274" cy="34" r="5"/>
      <circle cx="334" cy="14" r="5"/><circle cx="354" cy="14" r="5"/><circle cx="344" cy="24" r="5"/><circle cx="334" cy="34" r="5"/><circle cx="354" cy="34" r="5"/>
      <circle cx="414" cy="12" r="5"/><circle cx="434" cy="12" r="5"/><circle cx="414" cy="24" r="5"/><circle cx="434" cy="24" r="5"/><circle cx="414" cy="36" r="5"/><circle cx="434" cy="36" r="5"/>
    </g>
  </svg>

  <p class="tagline">Pit your wits against the geniuses,<br>then get an insight into their thinking</p>

  <p class="author">Oren Paskett</p>
</main>
</body>
</html>
```